We have 'joined together' 6 micro-sites with a common theme. Looking to upgrade the design of a total of 26 pages on the abovementioned sites, whilst maintaining a common look and feel.

Goal is to improve customer experience and conversion rate, whilst maintaining Vantro rankings. New design to be responsive to different devices and SEO optimised

We prefer simple designs with the cleaness of Zelqo.com, however with more descriptive text. Target audience are business managers and owners, so site should convey professional capability, with a hint of playfulness. After all data can be fun? No?

See attached doc for further details.

Update: 19/8/2014. Following further consideration, the HTML coding no longer required. Once design is finalised, we require a PSD file for each page showing the full page layout, including all images and icons. We will extract the relevant bits from the PSD and do the coding and css inhouse.
Updates

Hi All The Pelquin Collective - PSD Design Only. HTML no longer required Following further consideration, the HTML / Css coding aspect of the project NO longer required. Once design is finalised, we require a PSD file from you for each of the 26 web pages, showing the page layout and including all images and icons. If one page layout is the same as another, then we request that you just supply images and icons for that page in a PSD file. We will then extract the relevant bits from the PSD and we will do the coding and css inhouse. Our main aim is to get an awesome, blow-your-sox-off design that compels users to convert. Many thanks in anticipation Oliver.

Project Deadline Extended
Reason: Changed deliverables from PSD, HTML and Coding t o PSD only. Hopefully this change will allow previous designers who were not interested to reconsider. Many thanks Oliver

Target Market(s)

Target market is business & IT managers within Australian organisations who are having problems with their data. Site must convey the impression that we are:
1) Very capable
2) Professional in our dealings
3) Reliable & trustworthy
4) Just a little bit quirky

Aprox. 60% of users are female, 40% male. Typically in the 30 to 55 year old bracket.

Number 1 requirements is that we don't embarrass our clients in any way.
2nd is that we do a good high quality job, delivering a good result.

We are not the cheapest nor the most expensive data shop around. We offer good value-for-money solutions. We are also reliable, friendly and available

Industry/Entity Type

Business

Font styles to use
Sans Serif

Requirements
Must have
• Simple yet information dense design. The "who we are" and "what we do" to be immediately visible above the fold. Images to be high quality. Good usability.
Simple navigation structure. Easy for users to find the info that they want.

In summary a simple, but good looking site, that compels users to contact us
Should not have
• No flash, fancy automation, rotating images, pop-ups etc.

```html
<!DOCTYPE html>
<html lang="en">
<head>
<meta charset="utf-8">
<title>The Pelquin Collective</title>
<link rel="stylesheet" href="https://fonts.googleapis.com/css2?family=Montserrat:wght@800&family=PT+Sans:wght@400;700&family=Raleway:wght@500&display=swap">
<style>
:root{
  --blue:#1b8fd6;
  --ink:#1c1c1c;
  --text:#333;
  --heading:#444;
  --sky:#d4effb;
  --cloud-grey:#ececec;
  --field-line:#cfcfcf;
  --feed:#f5a01c;
  --bird:#2aa4e0;
  --social:#1957a5;
}
*{box-sizing:border-box;margin:0;padding:0}
html,body{width:1200px;height:2212px;overflow:hidden;background:#fff}
body{font-family:"PT Sans",sans-serif;color:var(--text)}
.page{position:relative;width:1200px;height:2212px;overflow:hidden}
.abs{position:absolute}

/* header */
.brand{left:123px;top:24px;font-family:"Montserrat",sans-serif;font-weight:800;font-size:28px;letter-spacing:.3px;color:var(--ink);white-space:nowrap}
.util{top:30px;left:742px;font-size:15px;color:var(--ink);white-space:nowrap}
.util span{margin:0 16px}
.phone{left:904px;top:22px;display:flex;align-items:center;gap:10px;color:var(--blue);font-size:22px;letter-spacing:1px}
.nav{top:88px;left:0;width:1200px;font-size:14px;color:var(--ink)}
.nav a{position:absolute;text-decoration:none;color:inherit;white-space:nowrap}
.nav a.active{color:var(--blue)}

/* hero */
.hero-sky{left:0;top:300px;width:1200px;height:380px;background:linear-gradient(to bottom,rgba(212,239,251,0) 0%,var(--sky) 25%,#e6f6fd 65%,#fff 100%)}
.hero-art{left:120px;top:158px;width:952px;height:382px;border-radius:190px 190px 40px 40px;background:radial-gradient(ellipse at 50% 60%,#2f8fdc 0%,#49b7ec 45%,#bfe8f9 80%,rgba(212,239,251,0) 100%)}

/* services */
.service{width:300px;text-align:center}
.service .icon{width:100px;height:100px;margin:0 auto;border-radius:14px;background:linear-gradient(135deg,#e9eef2,#bcc6ce 60%,#5fb8ea)}
.service h3{margin-top:28px;font-size:22px;font-weight:700;color:var(--heading);letter-spacing:.3px}

/* benefits */
.benefits-title{top:1046px;left:0;width:1200px;text-align:center;font-size:36px;font-weight:400;color:var(--ink);letter-spacing:.5px}
.benefits-intro{top:1108px;left:130px;width:940px;text-align:center;font-size:19px;line-height:29px;color:var(--ink)}
.benefit{left:120px;width:960px;display:flex;gap:20px}
.benefit svg{flex:none;margin-top:2px}
.benefit h4{font-size:22px;font-weight:700;color:var(--ink);line-height:28px}
.benefit p{font-size:15px;line-height:24px;color:var(--text);margin-top:2px}

/* footer */
.footer-band{left:0;top:1640px;width:1200px;height:180px;background:linear-gradient(to bottom,rgba(236,236,236,0) 0%,var(--cloud-grey) 30%,#f3f3f3 65%,#fff 100%)}
.contact-title{left:123px;top:1792px;font-size:24px;font-weight:400;color:var(--ink)}
.contact-sub{left:123px;top:1832px;font-size:13.5px;font-weight:700;color:var(--ink)}
.field{left:123px;border:1.5px solid var(--field-line);border-radius:4px;background:#fff;font-family:"Raleway",sans-serif;font-size:14px;color:#555;padding:12px 10px}
.send{left:123px;top:2121px;width:153px;height:40px;background:var(--blue);color:#fff;font-family:"Raleway",sans-serif;font-size:14px;display:flex;align-items:center;justify-content:center;letter-spacing:.5px}
.social{top:1800px;width:56px;height:52px}
.info{left:789px;top:1883px;font-size:13.5px;line-height:24.8px;color:var(--ink)}
</style>
</head>
<body>
<div class="page">

  <header>
    <div class="abs brand">THE PELQUIN COLLECTIVE</div>
    <div class="abs util">BLOG<span>|</span>CONTACT</div>
    <div class="abs phone">
      <svg width="30" height="30" viewBox="0 0 30 30" aria-hidden="true">
        <circle cx="15" cy="15" r="13.5" fill="none" stroke="#222" stroke-width="2"/>
        <path d="M10 8.5c1-.8 2-.6 2.6.4l1.3 2.2c.4.8.2 1.5-.5 2l-1 .7c.7 1.8 2 3.3 3.8 4.3l.8-.9c.6-.6 1.4-.7 2-.2l2 1.5c.9.7.9 1.7.1 2.6l-1 1c-1.3 1.2-4.5.2-7.2-2.5S8 11.3 9.2 9.4z" fill="#222"/>
      </svg>
      <span>1300 412 907</span>
    </div>
    <nav class="abs nav">
      <a class="active" style="left:153px">HOME</a>
      <a style="left:242px">PELQUIN</a>
      <a style="left:362px">DATA ANALYSIS</a>
      <a style="left:504px">DATA CLEANSING</a>
      <a style="left:657px">DATA MINING</a>
      <a style="left:786px">DATA SCRAPING</a>
      <a style="left:930px">DATA WAREHOUSE</a>
    </nav>
  </header>

  <section>
    <div class="abs hero-sky" role="img" aria-label="Soft band of pale blue clouds"></div>
    <div class="abs hero-art" role="img" aria-label="Illustration of glossy blue clouds carrying media, music, photo and document icons with an upload arrow"></div>
  </section>

  <section>
    <div class="abs service" style="left:116px;top:598px"><div class="icon" role="img" aria-label="Data analysis icon: rising bar chart with arrow"></div><h3>DATA ANALYSIS</h3></div>
    <div class="abs service" style="left:450px;top:598px"><div class="icon" role="img" aria-label="Data cleansing icon: bar chart with brush"></div><h3>DATA CLEANSING</h3></div>
    <div class="abs service" style="left:783px;top:598px"><div class="icon" role="img" aria-label="Data mining icon: connected blocks with magnifier"></div><h3>DATA MINING</h3></div>
    <div class="abs service" style="left:116px;top:804px"><div class="icon" role="img" aria-label="Data scraping icon: pie chart with candlesticks"></div><h3>DATA SCRAPING</h3></div>
    <div class="abs service" style="left:450px;top:804px"><div class="icon" role="img" aria-label="Data warehouse icon: tree of monitors"></div><h3>DATA WAREHOUSE</h3></div>
    <div class="abs service" style="left:783px;top:804px"><div class="icon" role="img" aria-label="Data resources icon: magnifier over signal line"></div><h3>DATA RESOURCES</h3></div>
  </section>

  <section>
    <h2 class="abs benefits-title">YOUR BENEFITS</h2>
    <p class="abs benefits-intro">Our core speciality is solving business problems that require complex <b>data analysis</b>, <b>cleansing</b>, <b>mining</b> or <b>modelling techniques</b>. Your benefits include:</p>

    <div class="abs benefit" style="top:1194px">
      <svg width="32" height="32" viewBox="0 0 32 32" aria-hidden="true"><rect x="2" y="5" width="25" height="25" rx="3" fill="#fff" stroke="#6b7680" stroke-width="2.5"/><path d="M8 16l5 6L29 3" fill="none" stroke="#1b8fd6" stroke-width="3.5" stroke-linecap="round"/></svg>
      <div><h4>Fast ROI</h4><p>Quick access to skilled data professionals, without the overhead of building and maintaining your own infrastructure and team. Our fees are typically small in contrast to the additional profits or savings that our projects generate for our clients.</p></div>
    </div>
    <div class="abs benefit" style="top:1298px">
      <svg width="32" height="32" viewBox="0 0 32 32" aria-hidden="true"><rect x="2" y="5" width="25" height="25" rx="3" fill="#fff" stroke="#6b7680" stroke-width="2.5"/><path d="M8 16l5 6L29 3" fill="none" stroke="#1b8fd6" stroke-width="3.5" stroke-linecap="round"/></svg>
      <div><h4>Innovative practical solutions</h4><p>We find smart ways to extract useful information from incomplete and disorganised data. We also have extensive industry experience AND the quantitative rigour to generate innovative yet pragmatic value-adding solutions.</p></div>
    </div>
    <div class="abs benefit" style="top:1401px">
      <svg width="32" height="32" viewBox="0 0 32 32" aria-hidden="true"><rect x="2" y="5" width="25" height="25" rx="3" fill="#fff" stroke="#6b7680" stroke-width="2.5"/><path d="M8 16l5 6L29 3" fill="none" stroke="#1b8fd6" stroke-width="3.5" stroke-linecap="round"/></svg>
      <div><h4>Connected to major universities</h4><p>We have relationships with leading practitioners at major universities and business schools within Australia. This provides us with ready access to extensive expertise and the latest developments. We have never turned down a project due to it being too complex.</p></div>
    </div>
    <div class="abs benefit" style="top:1504px">
      <svg width="32" height="32" viewBox="0 0 32 32" aria-hidden="true"><rect x="2" y="5" width="25" height="25" rx="3" fill="#fff" stroke="#6b7680" stroke-width="2.5"/><path d="M8 16l5 6L29 3" fill="none" stroke="#1b8fd6" stroke-width="3.5" stroke-linecap="round"/></svg>
      <div><h4>Always confidential and discreet</h4><p>We protect you data securely. All the data are encrypted and safe.</p></div>
    </div>
  </section>

  <footer>
    <div class="abs footer-band" role="img" aria-label="Faint grey cloud band behind the contact area"></div>

    <h2 class="abs contact-title">CONTACT US</h2>
    <p class="abs contact-sub">We'd love to discuss how we can help you. Call us on 1300 412 907 or submit the form below.</p>
    <div class="abs field" style="top:1876px;width:332px;height:41px">Name</div>
    <div class="abs field" style="top:1932px;width:332px;height:41px">Email</div>
    <div class="abs field" style="top:1989px;width:510px;height:116px">Message</div>
    <div class="abs send">SEND</div>

    <div class="abs social" style="left:789px;background:var(--feed)" role="img" aria-label="News feed link"></div>
    <div class="abs social" style="left:865px;background:var(--bird)" role="img" aria-label="Social profile link"></div>
    <div class="abs social" style="left:939px;background:var(--social)" role="img" aria-label="Community page link"></div>

    <div class="abs info">
      Phone :<br>1300 563 218<br>Fax :<br>+61 3 9461 3380<br>Our Sales Desk :Monday-Friday 9 to 5pm (AEST)<br><br>
      Melbourne :<br>41 Harlow Lane, South Melbourne, VIC 3205<br>Sydney :<br>115/8 Marlin St, Chatswood, Sydney (NSW) 2067
    </div>
  </footer>

</div>
</body>
</html>
```